E-mail Ad Design Project

I would like a lower banner ad designed for placement within an e-mail. The size has to be 450px x 230px (6in x 3.07in) and must be either a GIF or JPEG, not to exceed 30K.

We are a medical billing company that provides services to physical therapy practices in Florida, and this ad is intended for owners and office managers of physical therapy businesses. We provide therapy offices with practice management software, submit medical claims on behalf of their patients, follow-up with insurance companies on outstanding claims, and also perform necessary back-end collections with patient balances. We also are able to interface with popular therapy documentation products to streamline data entry.

The design colors should incorporate our logo and red/blue colors (see www.clinicianharbor.net).

Target Market(s)

Physical therapists and administrators of physical therapy offices

Industry/Entity Type

Physical Therapy

Requirements
Must have
• Grabbing/heading text:

Tired of Denials and Confusing Rejection Codes?
We Take the Pain Out of Medical Billing.

Offer:

Get Started Today with 2 Free Months of Billing
Nice to have
• We provide services mainly to Florida therapists, so it would be nice to have an image or text that highlights this fact. Also, the e-mail campaign this is a part of will be sent to Florida recipients.

```html
<!DOCTYPE html>
<html lang="en">
<head>
<meta charset="utf-8">
<title>Clinician Harbor – Email Banner</title>
<link href="https://fonts.googleapis.com/css2?family=Roboto+Condensed:wght@700&display=swap" rel="stylesheet">
<style>
  :root {
    --sky-top: #9ccbe9;
    --sky-low: #d6ebf5;
    --sea-light: #49aecd;
    --sea-deep: #2679ae;
    --sand: #e8d9b9;
    --white: #ffffff;
    --brand-blue: #2a4f86;
    --seal-red: #b01c22;
    --seal-ring: #e7b7b5;
    --text-shadow: rgba(10, 30, 60, 0.8);
  }
  * { margin: 0; padding: 0; box-sizing: border-box; }
  html, body {
    width: 1200px;
    height: 613px;
    overflow: hidden;
    background: var(--white);
  }
  .banner {
    position: relative;
    width: 1200px;
    height: 613px;
    overflow: hidden;
    font-family: "Roboto Condensed", "Arial Narrow", sans-serif;
    font-weight: 700;
    color: var(--white);
  }
  .beach-photo {
    position: absolute;
    inset: 0;
    background: linear-gradient(180deg,
      var(--sky-top) 0%,
      var(--sky-low) 36%,
      var(--sea-light) 48%,
      var(--sea-deep) 64%,
      var(--sea-light) 76%,
      var(--sand) 90%,
      var(--sand) 100%);
  }
  .brand-bar {
    position: absolute;
    left: 0;
    top: 0;
    width: 760px;
    height: 100px;
    background: linear-gradient(90deg, rgba(255,255,255,0.92) 0%, rgba(255,255,255,0.8) 70%, rgba(255,255,255,0) 100%);
    display: flex;
    align-items: center;
    padding-left: 80px;
    gap: 14px;
  }
  .brand-mark {
    width: 24px;
    height: 24px;
    background: var(--brand-blue);
  }
  .brand-name {
    color: var(--brand-blue);
    font-size: 34px;
    letter-spacing: 2px;
    text-transform: uppercase;
  }
  .headline {
    position: absolute;
    left: 40px;
    top: 126px;
    text-shadow: 0 3px 5px var(--text-shadow), 0 0 12px var(--text-shadow);
  }
  .headline-question {
    font-size: 59px;
    line-height: 1.26;
  }
  .headline-promise {
    margin-top: 4px;
    font-size: 74px;
    line-height: 1.2;
  }
  .offer-lead {
    position: absolute;
    left: 80px;
    top: 486px;
    font-size: 52px;
    text-shadow: 0 3px 5px var(--text-shadow), 0 0 12px var(--text-shadow);
  }
  .offer-seal {
    position: absolute;
    left: 605px;
    top: 315px;
    width: 294px;
    height: 294px;
  }
  .offer-seal svg { position: absolute; inset: 0; }
  .seal-text {
    position: absolute;
    inset: 0;
    display: flex;
    flex-direction: column;
    align-items: center;
    justify-content: center;
    text-align: center;
    font-size: 54px;
    line-height: 1.18;
    transform: rotate(-10deg);
  }
</style>
</head>
<body>
  <div class="banner">
    <div class="beach-photo" role="img" aria-label="Tropical beach with turquoise sea, palm fronds and two wooden deck chairs on the sand"></div>

    <div class="brand-bar">
      <div class="brand-mark"></div>
      <span class="brand-name">Clinician Harbor</span>
    </div>

    <div class="headline">
      <p class="headline-question">Tired of Denials and<br>Confusing Rejection Codes?</p>
      <p class="headline-promise">We Take the Pain Out<br>of Medical Billing.</p>
    </div>

    <p class="offer-lead">Get Started Today with</p>

    <div class="offer-seal">
      <svg viewBox="0 0 294 294" aria-hidden="true">
        <circle cx="147" cy="147" r="145" fill="var(--seal-red)"/>
        <circle cx="147" cy="147" r="130" fill="none" stroke="var(--seal-ring)" stroke-width="3" stroke-dasharray="6 5"/>
      </svg>
      <div class="seal-text">
        <span>2 Free</span>
        <span>Months of</span>
        <span>Billing</span>
      </div>
    </div>
  </div>
</body>
</html>
```